New business card design needed for Diesel Fitting (Mechanical) Company

We need a new business card for our company called "Gumtree Engine Works" that showcases our logo and business details.
Target Market(s)
Owners of all makes and models of vehicles, trucks, plant and machinery.
Industry/Entity Type
Mechanical
Contact Information for Business Card
The business card details need to include the following: Owners/Directors: Doug & Marisol Brent-Coyle ABN: 41 917 302 846 Address: 317 Wattlebrook Street WATTLE CREEK QLD 4899 Postal Address: PO Box 5791 WATTLE CREEK QLD 4899 Website: www.gewservice.com.au Phone: 4712 9083 Mobile: 0438 175 906 Emails: sales@gewservice.com.au; admin@gewservice.com.au; accounts@gewservice.com.au; parts@gewservice.com.au; office@gewservice.com.au, reception@gewservice.com.au
Look and feel

```html
<!DOCTYPE html>
<html lang="en">
<head>
<meta charset="utf-8">
<title>Gumtree Engine Works – Business Card</title>
<link href="https://fonts.googleapis.com/css2?family=Poppins:wght@600&family=Nunito+Sans:wght@400;600;800&display=swap" rel="stylesheet">
<style>
  :root {
    --stage: #3b3b3b;
    --paper: #ffffff;
    --charcoal: #232323;
    --charcoal-dark: #1b1b1b;
    --ink: #1a1a1a;
    --orange: #e96c24;
    --rust: #8e4a2e;
    --brown: #4a3a33;
    --yellow: #fdc216;
    --red: #e8262b;
    --rule-grey: #3d3d3d;
    --white: #ffffff;
  }
  html, body {
    margin: 0;
    width: 1200px;
    height: 1200px;
    overflow: hidden;
    background: var(--stage);
  }
  .canvas {
    position: relative;
    width: 1200px;
    height: 1200px;
  }
  .card {
    position: absolute;
    top: 222px;
    width: 487px;
    height: 812px;
    box-shadow: 0 10px 24px rgba(0,0,0,.35);
  }
  .card svg { display: block; width: 100%; height: 100%; }
  .card-front { left: 66px; }
  .card-back { left: 647px; }
  .brand-name { font-family: "Nunito Sans", sans-serif; font-weight: 800; fill: var(--ink); }
  .front-web { font-family: "Nunito Sans", sans-serif; font-weight: 800; fill: var(--white); }
  .holder-name { font-family: "Poppins", sans-serif; font-weight: 600; fill: var(--white); }
  .holder-role { font-family: "Nunito Sans", sans-serif; font-weight: 400; fill: var(--white); }
  .contact-line { font-family: "Nunito Sans", sans-serif; font-weight: 400; fill: var(--white); letter-spacing: .5px; }
  .contact-web { font-family: "Nunito Sans", sans-serif; font-weight: 800; fill: var(--white); }
</style>
</head>
<body>
<main class="canvas">

  <section class="card card-front" aria-label="Business card front">
    <svg viewBox="0 0 675 1125" xmlns="http://www.w3.org/2000/svg">
      <defs>
        <linearGradient id="darkWedge" x1="0" y1="0" x2="0" y2="1">
          <stop offset="0" stop-color="#2c2c2c"/>
          <stop offset="1" stop-color="#5a3a2c"/>
        </linearGradient>
        <linearGradient id="orangeBlock" x1="0" y1="0" x2="0" y2="1">
          <stop offset="0" stop-color="#c0612c"/>
          <stop offset="1" stop-color="#ec6d22"/>
        </linearGradient>
      </defs>
      <rect class="paper" width="675" height="1125" fill="var(--paper)"/>

      <g class="brand-block">
        <circle cx="337" cy="255" r="26" fill="var(--orange)"/>
        <text class="brand-name" x="337" y="390" font-size="52" text-anchor="middle">Gumtree Engine Works</text>
      </g>

      <polygon class="wedge-dark" points="0,438 368,628 0,795" fill="url(#darkWedge)"/>
      <polygon class="wedge-orange" points="156,912 675,680 675,1125 628,1125" fill="url(#orangeBlock)"/>
      <polygon class="wedge-rust" points="156,912 444,785 444,1041" fill="var(--rust)" opacity=".9"/>

      <g class="front-website" transform="translate(278,916)">
        <circle cx="0" cy="0" r="10" fill="none" stroke="var(--white)" stroke-width="2.5"/>
        <path d="M-10 0 H10 M0 -10 C-6 -4 -6 4 0 10 M0 -10 C6 -4 6 4 0 10" fill="none" stroke="var(--white)" stroke-width="2"/>
        <text class="front-web" x="23" y="9" font-size="26">www.gewservice.com</text>
      </g>
    </svg>
  </section>

  <section class="card card-back" aria-label="Business card back">
    <svg viewBox="0 0 675 1125" xmlns="http://www.w3.org/2000/svg">
      <rect width="675" height="1125" fill="var(--charcoal)"/>
      <rect class="pattern-zone" width="675" height="340" fill="var(--charcoal-dark)" opacity=".55" role="img" aria-label="Subtle dark diamond pattern"/>
      <polygon class="accent-yellow" points="345,333 675,185 675,333" fill="var(--yellow)"/>

      <text class="holder-name" x="83" y="176" font-size="38">Doug &amp; Marisol Brent-Coyle</text>
      <text class="holder-role" x="84" y="218" font-size="26">Owners/Directors</text>
      <rect class="rule-grey" x="83" y="241" width="310" height="3" fill="var(--rule-grey)"/>
      <rect class="rule-orange" x="83" y="241" width="155" height="4" fill="var(--orange)"/>

      <g class="icon-phone" transform="translate(83,393)">
        <rect width="62" height="58" fill="var(--red)"/>
        <path d="M18 22 Q31 12 44 22 L41 27 L37 25 V22 H25 V25 L21 27 Z M22 30 H40 L42 42 H20 Z" fill="var(--white)"/>
      </g>
      <text class="contact-line" x="176" y="418" font-size="30">4712 9083</text>
      <text class="contact-line" x="176" y="456" font-size="30">0438 175 906</text>

      <g class="icon-web" transform="translate(83,482)">
        <rect width="62" height="58" fill="var(--red)"/>
        <circle cx="31" cy="29" r="14" fill="none" stroke="var(--white)" stroke-width="3"/>
        <path d="M17 29 H45 M31 15 C23 22 23 36 31 43 M31 15 C39 22 39 36 31 43" fill="none" stroke="var(--white)" stroke-width="2.5"/>
      </g>
      <text class="contact-web" x="176" y="522" font-size="30">www.gewservice.com</text>

      <g class="icon-mail" transform="translate(83,577)">
        <rect width="62" height="58" fill="var(--red)"/>
        <rect x="15" y="18" width="32" height="22" fill="none" stroke="var(--white)" stroke-width="2.5"/>
        <path d="M15 18 L31 31 L47 18 M15 40 L27 28 M47 40 L35 28" fill="none" stroke="var(--white)" stroke-width="2.5"/>
      </g>
      <g class="email-list" font-size="30">
        <text class="contact-line" x="176" y="597">sales@gewservice.com.au</text>
        <text class="contact-line" x="176" y="634">admin@gewservice.com.au</text>
        <text class="contact-line" x="176" y="672">accounts@gewservice.com.au</text>
        <text class="contact-line" x="176" y="709">parts@gewservice.com.au</text>
        <text class="contact-line" x="176" y="746">office@gewservice.com.au</text>
        <text class="contact-line" x="176" y="784">reception@gewservice.com.au</text>
      </g>

      <g class="icon-pin" transform="translate(83,872)">
        <rect width="62" height="58" fill="var(--red)"/>
        <path d="M31 44 C24 34 20 29 20 23 A11 11 0 0 1 42 23 C42 29 38 34 31 44 Z" fill="var(--white)"/>
        <circle cx="31" cy="23" r="4" fill="var(--red)"/>
      </g>
      <g class="address" font-size="30">
        <text class="contact-line" x="176" y="897">317 Wattlebrook Street</text>
        <text class="contact-line" x="176" y="934">WATTLE CREEK</text>
        <text class="contact-line" x="176" y="972">QLD 4899</text>
        <text class="contact-line" x="176" y="1009">PO Box 5791</text>
      </g>
    </svg>
  </section>

</main>
</body>
</html>
```